Spring Menu Design for newly renovated, vibrant cafe with exciting food

We need a menu designed for our brand new Spring menu. We would like it to be landscape with a number of columns. I'd ideally like it to be two sided - with the front side having the cafe logo - and the rest of the menu on the other side. I do understand there may be too much content to achieve this. We would like greys and soft pinks used - with an easy to understand font, which exudes style and warmth. I have attached a photo of one of the cushions in the cafe. The staff are currently wearing this dusty pink - with grey aprons with black straps. Our logo is attached and includes red, black and grey. I don't want to see red on the menu - except for a discreet heart placed somewhere within the design. Please feel free to contact me for more info. Looking forward to seeing exciting designs

Requirements
Must have
• Clean design
• Blush pink and grey feel
• landscape
Nice to have
• Front side for logo, second side for menu
Should not have
• No frumpy, bulky looks

```html
<!DOCTYPE html>
<html lang="en">
<head>
<meta charset="utf-8">
<title>Bloomwell café – Spring Menu</title>
<link href="https://fonts.googleapis.com/css2?family=Montserrat:ital,wght@0,300;0,400;0,600;1,400&family=Mr+Dafoe&display=swap" rel="stylesheet">
<style>
  :root {
    --backdrop: #e7e3df;
    --marble-light: #f6f6f6;
    --marble-mid: #e6e6e8;
    --blush: #e9d3d6;
    --ink: #1c1c1c;
    --soft-ink: #3a3a3a;
    --frame-grey: #9a9a9e;
    --heart: #d0141c;
    --body: 'Montserrat', Arial, sans-serif;
    --script: 'Mr Dafoe', cursive;
  }
  * { box-sizing: border-box; margin: 0; padding: 0; }
  html, body { width: 1200px; height: 1200px; overflow: hidden; background: var(--backdrop); }
  .stage { position: relative; width: 1500px; height: 1500px; transform: scale(0.8); transform-origin: 0 0; font-family: var(--body); color: var(--ink); }

  .sheet { position: absolute; width: 940px; height: 664px;
    background: linear-gradient(135deg, var(--marble-light) 0%, var(--marble-mid) 35%, var(--marble-light) 55%, var(--marble-mid) 80%, var(--marble-light) 100%);
    box-shadow: 0 2px 8px rgba(0,0,0,.12); }

  /* Front cover */
  .cover { left: 45px; top: 50px; height: 663px; }
  .cover-frame { position: absolute; left: 18px; top: 18px; right: 18px; bottom: 18px; border: 2px solid var(--frame-grey); }
  .cover-name { position: absolute; left: 0; right: 0; top: 312px; text-align: center; font-size: 36px; font-weight: 300; letter-spacing: 1px; color: var(--ink); }

  /* Menu side */
  .menu { left: 497px; top: 773px; }
  .blush-panel { position: absolute; left: 0; top: 0; width: 516px; height: 550px; background: var(--blush); }
  .script-title { font-family: var(--script); font-weight: 400; font-size: 34px; color: var(--ink); position: absolute; line-height: 1; }
  .brunch-title { left: 86px; top: 24px; }
  .dot { position: absolute; width: 6px; height: 6px; border-radius: 50%; background: var(--ink); top: 42px; }

  .lunch-frame { position: absolute; left: 276px; top: 34px; width: 206px; height: 133px; border: 2px solid var(--ink); }
  .lunch-frame-inner { position: absolute; left: 287px; top: 26px; width: 186px; height: 148px; border: 1px solid #fff; }
  .lunch-tab { position: absolute; left: 321px; top: 0; width: 115px; height: 64px; background: #fff; }
  .lunch-title { left: 348px; top: 22px; font-size: 30px; }
  .lunch-note { position: absolute; left: 298px; top: 76px; width: 160px; font-size: 8.6px; line-height: 12px; text-align: justify; text-align-last: center; }

  .item { position: absolute; font-size: 9px; line-height: 12px; color: var(--soft-ink); }
  .item-name { font-size: 11px; font-weight: 600; color: var(--ink); line-height: 14px; }
  .price { position: absolute; right: 0; top: 0; font-size: 11px; color: var(--ink); }
  .addon { font-size: 7.4px; font-style: italic; text-transform: uppercase; display: flex; justify-content: space-between; }
  .addon b { font-style: normal; font-weight: 600; font-size: 9px; }
  .brunch-col { left: 35px; width: 208px; }
  .brunch-col .desc { width: 170px; }
  .lunch-col { left: 275px; width: 208px; }
  .lunch-col .desc { width: 180px; }

  .band { position: absolute; left: 568px; width: 372px; background: var(--blush); }
  .kids-band { top: 35px; height: 33px; }
  .drink-band { top: 254px; height: 43px; }
  .kids-title { left: 602px; top: 42px; font-size: 28px; }
  .drink-title { left: 602px; top: 262px; font-size: 30px; }
  .rule { position: absolute; left: 550px; width: 2px; background: var(--ink); }
  .rule-kids { top: 67px; height: 200px; }
  .rule-drink { top: 287px; height: 377px; }
  .rule-tick { position: absolute; left: 550px; height: 2px; width: 18px; background: var(--ink); }

  .kids-col { left: 582px; width: 140px; }
  .kids-col-2 { left: 780px; width: 120px; }
  .drink-col { left: 583px; width: 318px; }
  .item small { font-size: 7.4px; }
  .sized { position: relative; display: inline-block; margin-left: 8px; text-align: center; }
  .sized i { position: absolute; left: 0; right: 0; top: -7px; font-size: 4.5px; line-height: 5px; font-style: normal; }

  .legend { position: absolute; left: 35px; top: 577px; font-size: 9px; line-height: 12px; display: grid; grid-template-columns: 48px 100px; }
  .notice { position: absolute; left: 233px; top: 580px; width: 282px; height: 52px; background: var(--blush); font-size: 8.4px; font-variant: small-caps; letter-spacing: .3px; text-align: center; padding-top: 13px; line-height: 12px; }
  .heart { position: absolute; width: 8px; height: 8px; }
</style>
</head>
<body>
<div class="stage">

  <section class="sheet cover">
    <div class="cover-frame"></div>
    <div class="cover-name">Bloomwell café</div>
  </section>

  <section class="sheet menu">
    <div class="blush-panel"></div>

    <span class="dot" style="left:62px"></span>
    <h2 class="script-title brunch-title">Brunch</h2>
    <span class="dot" style="left:206px"></span>

    <div class="item brunch-col" style="top:80px"><div class="item-name">Toast</div><div class="desc">Seeded sourdough / Brioche fruit loaf, with your choice of Ridgeline Preserve raspberry jam, Bayside Honey, savourite, or Marlo's Peanut Butter (VGA) (GFA)</div><span class="price">$8.5</span></div>
    <div class="item brunch-col" style="top:168px"><div class="item-name">Forage Granola</div><div class="desc">Almonds, macadamia nuts, sunflower seeds, pepitas, currants, pecan nuts, dates, cranberries and coconut, Spring fruits, Oat Barn almond milk (GF) (Vegan) (DF) (Paleo)</div><span class="price">$15</span></div>
    <div class="item brunch-col" style="top:256px"><div class="item-name">Waffles</div><div class="desc">Golden waffles, ice-cream, honeycomb, warm chocolate drizzle, strawberries &nbsp;(V)</div><span class="price">$16</span></div>
    <div class="item brunch-col" style="top:309px"><div class="item-name">Persian Eggs</div><div class="desc">Free range poached eggs, walnut and pomegranate crumble, Persian fetta, roasted tomatoes, sourdough, sumac, watercress &nbsp;(V) (GFA)</div><span class="price">$17</span></div>
    <div class="item brunch-col" style="top:385px"><div class="item-name">Bruschetta</div><div class="desc">Sautéed herby mushrooms, hummus, goat cheese, sourdough, Sticky Truffle Balsamic &nbsp;(V) (GFA)</div><span class="price">$18</span></div>
    <div class="item brunch-col" style="top:449px"><div class="item-name">Fritters</div><div class="desc">Sweet corn fritters, medley tomatoes, micro greens, poached egg, chilli, coriander, avocado and lime green goddess dressing &nbsp;(V)</div>
      <div class="addon" style="width:135px">* Add premium bacon <b>$4.5</b></div><span class="price">$20</span></div>

    <div class="lunch-frame"></div>
    <div class="lunch-frame-inner"></div>
    <div class="lunch-tab"></div>
    <h2 class="script-title lunch-title">lunch</h2>
    <p class="lunch-note">We offer lunch via our specials board to make the best use of the produce which comes our way. Simpler options are available in our display case. Please order and pay at the counter.</p>

    <div class="item lunch-col" style="top:191px"><div class="item-name">Bloomwell Smash</div><div class="desc">House-made pumpkin loaf, avocado, basil and pine nut pesto, baby tomato salsa, Hillcrest goat cheese, leaves, Sticky Fig Balsamic<br>(V) (GFA) (VGA) DFA)</div>
      <div class="addon" style="width:135px;margin-top:4px">* Add free range egg <b>$2.5</b></div>
      <div class="addon" style="width:135px">* Add premium bacon <b>$4.5</b></div><span class="price">$20</span></div>
    <div class="item lunch-col" style="top:308px"><div class="item-name">Benny Two Ways</div><div class="desc">Premium bacon OR sautéed herby mushrooms, two free range poached eggs, spinach hollandaise, seeded sourdough (Mushroom version V)</div><span class="price">$21</span></div>
    <div class="item lunch-col" style="top:385px"><div class="item-name">Eggs Your Way</div><div class="desc" style="width:172px">Two free range eggs, poached, fried or scrambled, seeded sourdough, butter, if you wish<br>(V) (GFA)</div>
      <div class="addon" style="margin-top:4px">* Additions:</div>
      <div class="addon">Bacon - Avocado <b>$4.5</b></div>
      <div class="addon">Hillcrest goat feta - Sautéed mushrooms <b>$4</b></div>
      <div class="addon">Slow roasted tomatoes <b>$3.5</b></div>
      <div class="addon">Hollandaise - Spinach - Free range egg <b>$2.5</b></div>
      <div class="addon">Tomato relish <b>$2</b></div><span class="price">$13.5</span></div>

    <div class="band kids-band"></div>
    <h2 class="script-title kids-title">kids only</h2>
    <div class="rule rule-kids"></div>
    <div class="rule-tick" style="top:67px"></div>
    <div class="rule-tick" style="top:265px"></div>

    <div class="item kids-col" style="top:93px"><div class="item-name">Choc Puffs</div>With milk<span class="price">$3.5</span></div>
    <div class="item kids-col" style="top:132px"><div class="item-name">Berries</div>With natural yogurt<span class="price">$6</span></div>
    <div class="item kids-col" style="top:171px"><div class="item-name">Croissant</div>Ham and cheese<span class="price">$8.5</span></div>
    <div class="item kids-col" style="top:210px"><div class="item-name">Toastie</div>Ham, cheese and tomato<span class="price">$8.5</span></div>
    <div class="item kids-col-2" style="top:93px"><div class="item-name">Little Eggs</div><div style="width:88px;font-size:8.2px;line-height:11px">Scrambled eggs with buttered toast soldiers</div><span class="price">$10</span></div>
    <div class="item kids-col-2" style="top:153px"><div class="item-name">The Lunch Box</div><div style="width:92px;font-size:8.2px;line-height:11.5px">Savourite and cheese sandwich triangles, vegie sticks, dips, fruit and yogurt cup in a cute carboard lunch box</div><span class="price">$10</span></div>

    <div class="band drink-band"></div>
    <h2 class="script-title drink-title">Drink</h2>
    <div class="rule rule-drink"></div>
    <div class="rule-tick" style="top:287px"></div>

    <div class="item drink-col" style="top:315px"><div class="item-name">Coffee</div>by Morning Coffee, Pelican Bay<span class="price"><span class="sized"><i>Cup</i>$4</span><span class="sized"><i>Mug</i>$4.5</span></span></div>
    <div class="item drink-col" style="top:354px"><div class="item-name">Not Coffee</div>Hot chocolate, Dirty Chai, Chai latte (leaves, or powder)</div>
    <div class="item drink-col" style="top:393px"><div class="item-name">Organic Leaf Tea</div><small>English Breakfast / Earl Grey / Camomile / Peppermint / Mother Earth /<br>Liquorice Twist / Lemongrass &amp; Ginger / Green / Original Chai</small><span class="price">$4.5</span></div>
    <div class="item drink-col" style="top:442px"><div class="item-name">Organic Orange Juice</div><span class="price"><span class="sized"><i>Glass</i>$7</span></span></div>
    <div class="item drink-col" style="top:469px"><div class="item-name">Milkshakes</div><small>Chocolate / Strawberry / Caramel / Vanilla / Soy / Almond / Coconut <b>(+$1.5)</b></small><span class="price">$6.5</span></div>
    <div class="item drink-col" style="top:507px"><div class="item-name">Iced Drinks</div><div style="font-size:8px;font-weight:600;font-variant:small-caps">Coffee / Chocolate / Mocha</div>Served with ice-cream &amp; whipped cream<br>Soy / Almond / Coconut <b>(+$1.5)</b><span class="price">$7</span></div>
    <div class="item drink-col" style="top:569px"><div class="item-name">Spider</div>Any of our fizzy flavours over ice cream <i>(see fridge for selection)</i><span class="price">$7</span></div>
    <div class="item drink-col" style="top:608px"><div class="item-name">Smoothies</div><i>(Please check counter for today's selection)</i></div>

    <div class="legend">
      <span>• (V)</span><span>Vegetarian</span>
      <span>• (VGA)</span><span>Vegan Available</span>
      <span>• (DF)</span><span>Dairy Free</span>
      <span>• (GF)</span><span>Gluten Free</span>
      <span>• (GFA)</span><span>Gluten Free Available</span>
    </div>
    <div class="notice">
      Please order and pay at the counter. Thank you!<br>A 10% surcharge is applied on public holidays
      <svg class="heart" style="left:13px;top:28px" viewBox="0 0 10 10" aria-hidden="true"><path d="M5 9 L1 5 A2.2 2.2 0 0 1 5 2 A2.2 2.2 0 0 1 9 5 Z" fill="var(--heart)"/></svg>
      <svg class="heart" style="right:16px;top:26px" viewBox="0 0 10 10" aria-hidden="true"><path d="M5 9 L1 5 A2.2 2.2 0 0 1 5 2 A2.2 2.2 0 0 1 9 5 Z" fill="var(--heart)"/></svg>
    </div>
  </section>

</div>
</body>
</html>
```